Gerald Pinnock - Corporate MC & Entertainer

Design a one page A4 flyer
(See Brief Attached)
I'm after a one Page Flyer
A4 Size - One sided
I want the finished artwork in 2 Forms.
1/ One that I could print out myself in a small run ( I have a Dorvan Tint PrintMaster)
or send out as a PDF
2/ A second version that could be printed commercially , so including bleed crop marks so it can be cut to A4 size
I have attached the copy that should be included. (Agency Sweep 2014 WORDS)
If there was too much text to include , we could drop one of the testimonial quotes
I have attached 3 images that could be included if there is room.
If there were too many images I suggest dropping Image 3 ( with bow tie)
As you can see from the copy (or a visit to my website) there are two main services that I provide
Corporate MC Services and Entertainment Services.
These are however intertwined - My MC work often includes some entertaining effects from my ThoughtCatcher Show. I often get booked to MC a conference and provide a show.
I'm after something that is -
Classy , Sophisticated, Smart, perhaps a bit quirky.
Nothing "Magic" like - eg no Rabbits , Wands, puffs of smoke
I have no corporate colour or logo or branding that should be included
You can see some previous flyers here http://www.proflinkora.com/in/geraldpinnock
I like these, but looking for new ideas
Target Market(s)
Corporate , Conference Organisers, Speaker Bureau owners, Large Association Conference committees
Industry/Entity Type
Entertainment
Colors
Designer to choose colors to be used in the design.

```html
<!DOCTYPE html>
<html lang="en">
<head>
<meta charset="utf-8">
<title>Gerald Pinnock – Corporate MC &amp; Entertainer Flyer</title>
<link href="https://fonts.googleapis.com/css2?family=Roboto+Condensed:wght@300;400;700&display=swap" rel="stylesheet">
<style>
  :root {
    --stage: #e6e6e6;
    --flyer-bg: #050505;
    --accent: #1e9fd0;
    --text-grey: #9a9a9a;
    --text-white: #ffffff;
    --rule: #1e9fd0;
  }
  html, body {
    margin: 0;
    padding: 0;
    width: 948px;
    height: 1200px;
    overflow: hidden;
    background: var(--stage);
  }
  .flyer {
    position: absolute;
    left: 50px;
    top: 0;
    width: 848px;
    height: 1200px;
    background: var(--flyer-bg);
    font-family: "Roboto Condensed", "Arial Narrow", sans-serif;
    color: var(--text-white);
    overflow: hidden;
  }
  .flyer p { margin: 0; }
  .hero-photo {
    position: absolute;
    left: 0;
    top: 0;
    width: 848px;
    height: 530px;
    background:
      radial-gradient(ellipse 260px 300px at 270px 250px, #5a4c44 0%, #2a2522 45%, rgba(5,5,5,0) 100%),
      radial-gradient(ellipse 200px 110px at 700px 480px, #2a1a14 0%, rgba(5,5,5,0) 100%),
      var(--flyer-bg);
  }
  .headline {
    position: absolute;
    right: 62px;
    top: 130px;
    margin: 0;
    text-align: center;
    font-weight: 400;
    line-height: 1;
    text-shadow: 0 0 6px rgba(0,0,0,.6);
  }
  .headline .line1 { display: block; height: 50px; }
  .headline .big { font-size: 46px; }
  .headline .small { font-size: 32px; }
  .headline .line2 { display: block; font-size: 38px; }
  .identity {
    position: absolute;
    top: 530px;
    left: 0;
    width: 848px;
    display: flex;
    justify-content: center;
    align-items: center;
    gap: 12px;
  }
  .identity .name {
    color: var(--accent);
    font-size: 40px;
    font-weight: 400;
  }
  .identity .tagline {
    font-family: Arial, Helvetica, sans-serif;
    font-size: 15px;
    line-height: 1.1;
  }
  .identity .tagline .role { color: var(--text-grey); font-size: 16px; }
  .copy {
    position: absolute;
    left: 0;
    width: 848px;
    text-align: center;
    white-space: nowrap;
  }
  .venues {
    top: 609px;
    color: var(--text-grey);
    font-size: 26px;
    font-weight: 300;
    line-height: 36px;
  }
  .venues strong { font-weight: 700; }
  .summits {
    top: 729px;
    font-size: 19px;
    font-weight: 700;
    line-height: 26px;
  }
  .clients {
    top: 822px;
    color: var(--text-grey);
    font-size: 21px;
    font-weight: 300;
    line-height: 31px;
  }
  .travels-intro {
    top: 926px;
    color: var(--text-grey);
    font-size: 19px;
    font-weight: 300;
    line-height: 24px;
  }
  .ports {
    top: 951px;
    font-size: 33px;
    line-height: 36px;
  }
  .travels-tail {
    top: 992px;
    color: var(--text-grey);
    font-size: 16px;
    font-weight: 300;
    line-height: 20px;
  }
  .cta-prompt {
    top: 1038px;
    color: var(--accent);
    font-size: 25px;
    line-height: 30px;
  }
  .cta-site {
    top: 1065px;
    font-size: 33px;
    line-height: 36px;
  }
  .footer-rule {
    position: absolute;
    left: 0;
    top: 1117px;
    width: 848px;
    height: 2px;
    background: var(--rule);
  }
  .testimonial {
    position: absolute;
    margin: 0;
    font-family: Arial, Helvetica, sans-serif;
    font-size: 10px;
    line-height: 1.35;
  }
  .testimonial cite { font-style: normal; font-size: 5px; }
  .testimonial.first { left: 117px; top: 1134px; width: 290px; }
  .testimonial.second { left: 445px; top: 1146px; width: 320px; }
</style>
</head>
<body>
  <main class="flyer">
    <div class="hero-photo" role="img" aria-label="Photograph of a smiling grey-haired presenter in a dark suit and blue tie pointing upward beside a lectern microphone, against a black backdrop of soft scattered lights"></div>

    <h1 class="headline">
      <span class="line1"><span class="big">Solving</span> <span class="small">your</span></span>
      <span class="line2">Conference Puzzles!</span>
    </h1>

    <div class="identity">
      <span class="name">Gerald Pinnock</span>
      <span class="tagline">"Australia's Magician of the Mind"<br><span class="role">Corporate MC &nbsp;&amp;&nbsp; Entertainer</span></span>
    </div>

    <p class="copy venues">In the last two years Gerald has been engaged as the<br>Conference MC for events in <strong>Hawaii, New Zealand,</strong><br><strong>Hong Kong &amp; all States of Australia.</strong></p>
    <p class="copy summits">He facilitated 24 Australian Major Project<br>Conferences for FairVista and 16 International<br>CEO Summits for Meridel Global.</p>
    <p class="copy clients">In the Australian Corporate Sector, he managed major events for<br>OzLedger, NBRA, Homewell, Dial Leasing, ChapelCare and the<br>Seedling &amp; Grove Society.</p>
    <p class="copy travels-intro">As an Entertainer he cruised the world on several luxury cruise ships, visiting</p>
    <p class="copy ports">Japan, Korea, China, Tahiti and New Zealand</p>
    <p class="copy travels-tail">in his travels.</p>
    <p class="copy cta-prompt">What's coming up in 2014? &nbsp;Get involved at</p>
    <p class="copy cta-site">www.geraldpinnock.com</p>

    <div class="footer-rule"></div>

    <blockquote class="testimonial first">"Huge thanks for your professionalism with the Awards, getting a laugh from everyone and in general creating an atmosphere that was enjoyable and relaxed!" <cite>Homewell</cite></blockquote>
    <blockquote class="testimonial second">"A big thank you for a really good job on Friday night which was carried out with aplomb - &nbsp;well done!" <cite>Seedling &amp; Grove Society</cite></blockquote>
  </main>
</body>
</html>
```